Business card design needed

I need a business card for my private practice. I would like to see the designs that use bright blue and white. I would like to see similar designs as to the card below:
http://blog.printvarno.com/2009/designing-a-business-card-with-pv-ks517-template.html
I would like to see the back of the card have room for appointment times. Thank you.

Industry/Entity Type
Business
Contact Information for Business Card
Brightwater Counselling & Wellness Services
Helen Dorsey B.Psychology
Registered Psychologist
Building C, Level 3, 14 Marrow Crescent, Canberra, ACT 2601
T: (02) 6287 5912
F: (02) 6287 5930
info@brightwatercounselling.com.au
www.brightwatercounselling.com.au

```html
<!DOCTYPE html>
<html lang="en">
<head>
<meta charset="utf-8">
<title>Brightwater Counselling &amp; Wellness Services – Business Card</title>
<link rel="stylesheet" href="https://fonts.googleapis.com/css2?family=Archivo+Narrow:ital,wght@0,700;1,400&family=Oswald:wght@700&family=Roboto:wght@400&display=swap">
<style>
  :root {
    --card-blue: #0a3a85;
    --stripe-blue: #1a3a74;
    --curve-light: rgba(255, 255, 255, 0.16);
    --curve-clear: rgba(255, 255, 255, 0);
    --white: #ffffff;
    --soft-white: #e4e8f0;
  }
  html, body {
    margin: 0;
    padding: 0;
    width: 1200px;
    height: 695px;
    overflow: hidden;
    background: var(--card-blue);
  }
  .card {
    position: relative;
    width: 1200px;
    height: 695px;
    overflow: hidden;
    background: var(--card-blue);
    color: var(--white);
  }
  .stripe {
    position: absolute;
    top: 0;
    height: 695px;
    background: var(--stripe-blue);
  }
  .stripe--wide { left: 100px; width: 138px; }
  .stripe--middle { left: 247px; width: 30px; }
  .stripe--thin { left: 292px; width: 8px; }
  .curve-area {
    position: absolute;
    background: radial-gradient(ellipse at center, var(--curve-light) 0%, var(--curve-clear) 70%);
  }
  .curve-area--upper { left: 520px; top: 60px; width: 300px; height: 250px; }
  .curve-area--lower { left: 860px; top: 395px; width: 340px; height: 300px; }
  .practitioner {
    position: absolute;
    left: 169px;
    top: 110px;
    font-family: "Archivo Narrow", "Arial Narrow", sans-serif;
    line-height: 1.1;
  }
  .practitioner-name {
    margin: 0;
    font-size: 25px;
    font-weight: 700;
    letter-spacing: 0.8px;
    text-transform: uppercase;
  }
  .practitioner-degree {
    margin-left: 5px;
    font-size: 22px;
    font-weight: 400;
    font-style: italic;
    letter-spacing: 0;
    text-transform: none;
  }
  .practitioner-title {
    margin: 3px 0 0;
    font-family: "Roboto", Arial, sans-serif;
    font-size: 20px;
    color: var(--soft-white);
  }
  .practice-name {
    position: absolute;
    left: 0;
    top: 282px;
    width: 1200px;
    margin: 0;
    font-family: "Oswald", "Impact", sans-serif;
    font-weight: 700;
    font-size: 60px;
    line-height: 66px;
    letter-spacing: 3px;
  }
  .practice-name-line { display: block; white-space: nowrap; }
  .practice-name-line--first { padding-left: 410px; }
  .practice-name-line--second { padding-left: 498px; }
  .contact {
    position: absolute;
    right: 138px;
    top: 503px;
    font-family: "Roboto", Arial, sans-serif;
    font-style: normal;
    font-size: 23px;
    line-height: 35px;
    letter-spacing: 0.4px;
    text-align: right;
  }
  .contact-line { margin: 0; white-space: nowrap; }
  .contact-item { display: inline-flex; align-items: center; gap: 6px; }
  .contact-item + .contact-item { margin-left: 38px; }
  .contact-icon { width: 22px; height: 24px; }
</style>
</head>
<body>
  <main class="card">
    <div class="stripe stripe--wide"></div>
    <div class="stripe stripe--middle"></div>
    <div class="stripe stripe--thin"></div>
    <div class="curve-area curve-area--upper" role="img" aria-label="Sweeping white curve decoration"></div>
    <div class="curve-area curve-area--lower" role="img" aria-label="Sweeping white curve decoration"></div>

    <header class="practitioner">
      <h2 class="practitioner-name">Helen Dorsey<span class="practitioner-degree">B.Psychology</span></h2>
      <p class="practitioner-title">Registered Psychologist</p>
    </header>

    <h1 class="practice-name">
      <span class="practice-name-line practice-name-line--first">Brightwater Counselling</span>
      <span class="practice-name-line practice-name-line--second">&amp; Wellness Services</span>
    </h1>

    <address class="contact">
      <p class="contact-line">Building C, Level 3, 14 Marrow Crescent, Canberra, ACT 2601</p>
      <p class="contact-line">
        <span class="contact-item">
          <svg class="contact-icon" viewBox="0 0 22 24" aria-label="Phone">
            <rect x="6" y="2" width="10" height="20" rx="2" fill="#8fd0ff"/>
            <rect x="8" y="5" width="6" height="6" fill="#2a6fb0"/>
            <rect x="8" y="13" width="6" height="6" fill="#dff2ff"/>
          </svg>(02) 6287 5912
        </span>
        <span class="contact-item">
          <svg class="contact-icon" viewBox="0 0 22 24" aria-label="Fax">
            <rect x="6" y="2" width="10" height="7" fill="#ffffff"/>
            <rect x="2" y="9" width="18" height="9" rx="1" fill="#c9ccd2"/>
            <rect x="6" y="15" width="10" height="7" fill="#ffffff"/>
          </svg>(02) 6287 5930
        </span>
      </p>
      <p class="contact-line">
        <span class="contact-item">info@brightwatercounselling.com.au</span>
        <span class="contact-item">www.brightwatercounselling.com.au</span>
      </p>
    </address>
  </main>
</body>
</html>
```